Landing Page für Anbieter von Finanzierungslösungen
Zielgruppe
Finanzierungslösungen für Gewerbe und Firmen. Fokus liegt auf der Finanzierung von Rechenzentren und deren Einrichtung.
Aufgabenstellung
Wir haben bereits Visitenkarten und Briefbögen designen lassen. Bitte daran anlehnen.

```html
<!DOCTYPE html>
<html lang="de">
<head>
<meta charset="utf-8">
<title>Finoval – Finanzierung für Gewerbe und Firmen</title>
<link href="https://fonts.googleapis.com/css2?family=Inter:wght@400;500;600;700&display=swap" rel="stylesheet">
<style>
:root{
  --green:#7bc143;
  --dark:#2e3436;
  --dark-2:#3b4245;
  --panel:#40474a;
  --blue:#1a6db3;
  --text:#2a2f31;
  --muted:#5b6366;
  --line:#dfe3e5;
  --light:#f1f3f2;
  --white:#ffffff;
}
*{box-sizing:border-box;margin:0;padding:0}
html,body{width:1200px;height:3539px;overflow:hidden}
body{font-family:"Inter",Arial,sans-serif;color:var(--text);background:var(--white);position:relative}
.abs{position:absolute}
.eyebrow{font-size:12px;font-weight:600;color:var(--green);text-transform:uppercase;letter-spacing:.2px}
.btn{display:inline-flex;align-items:center;justify-content:center;font-weight:600;font-size:15px;border-radius:4px}
.btn-green{background:var(--green);color:var(--text)}
.btn-ghost{border:1px solid rgba(255,255,255,.7);color:#fff}

/* hero */
.hero{left:0;top:0;width:1200px;height:810px;background:var(--dark-2);overflow:hidden}
.hero-photo{left:0;top:0;width:1200px;height:810px;background:linear-gradient(90deg,#3e4548 0%,#6f7679 40%,#8b9295 55%,#4b5255 80%,#3a4043 100%);opacity:.9}
.hero-shade{left:0;top:0;width:1200px;height:810px;background:linear-gradient(90deg,rgba(50,56,58,.85) 0%,rgba(50,56,58,.45) 55%,rgba(50,56,58,.6) 100%)}
.hero-cut{left:0;top:0;width:1200px;height:810px}
.logo{left:56px;top:20px;color:#fff}
.logo b{font-size:27px;font-weight:700;display:flex;align-items:center;gap:8px;line-height:32px}
.logo b i{width:12px;height:12px;border-radius:50%;background:var(--green);display:inline-block}
.logo span{font-size:11px;font-weight:500;display:block;margin-top:1px}
.menu{left:448px;top:33px;display:flex;gap:40px;color:#fff;font-size:15px}
.nav-cta{left:983px;top:20px;width:154px;height:45px;border:1px solid rgba(255,255,255,.8);border-radius:5px;color:#fff;font-size:15px;font-weight:600}
.hero-eyebrow{left:61px;top:160px}
.hero-title{left:61px;top:203px;width:660px;color:#fff;font-size:41px;line-height:47px;font-weight:700}
.hero-text{left:61px;top:332px;width:560px;color:#fff;font-size:15px;line-height:18.5px}
.chips{left:61px;top:430px;display:flex;gap:13px}
.chip{height:36px;padding:0 17px;background:rgba(255,255,255,.15);border-radius:4px;color:#fff;font-size:14px;font-weight:600;display:flex;align-items:center}
.hero-btns{left:61px;top:530px;display:flex;gap:18px}
.hero-btns .btn{height:45px}

.quick{left:734px;top:160px;width:358px;height:445px;background:#fff;border-radius:6px;padding:30px 33px}
.quick h2{font-size:21px;line-height:28px;font-weight:700;margin-top:9px}
.field{height:45px;border:1px solid var(--line);border-radius:4px;font-size:12px;color:#9aa1a4;display:flex;align-items:center;padding:0 13px;justify-content:space-between}
.quick .field{margin-top:25px}
.quick .btn{width:100%;height:45px;margin-top:25px}
.note{font-size:10px;color:var(--muted);margin-top:18px}

.features{left:66px;top:683px;width:1026px;height:125px;background:#fff;border-radius:6px;box-shadow:0 3px 8px rgba(0,0,0,.15);display:flex;align-items:center}
.feature{flex:1;display:flex;gap:14px;padding:0 0 0 48px;height:90px;align-items:flex-start;border-right:1px solid var(--line)}
.feature:last-child{border:none}
.feature .ic{width:40px;height:40px;border-radius:50%;background:#eaf3e1;display:flex;align-items:center;justify-content:center;flex:none}
.feature h3{font-size:17px;font-weight:600;color:var(--blue);margin-top:8px}
.feature p{font-size:15px;line-height:18px;color:var(--muted);margin-top:12px}

/* sections */
.center{text-align:center;width:1200px;left:0}
.sec-title{font-size:26px;font-weight:700}
.sec-sub{font-size:15px;color:var(--muted)}
.card{border:1px solid var(--line);border-radius:4px;background:#fff;padding:0 30px}
.card .ico{width:45px;height:45px;border-radius:50%;background:var(--blue);margin-top:28px;display:flex;align-items:center;justify-content:center}
.card h3{font-size:17px;font-weight:600;margin-top:21px}
.card p{font-size:15px;line-height:18.5px;color:var(--muted);margin-top:16px}

.risk{left:0;top:1357px;width:1200px;height:366px;background:var(--dark)}
.risk-copy{left:67px;top:68px;width:520px;color:#fff}
.risk-copy h2{font-size:28px;font-weight:700;margin-top:21px;white-space:nowrap}
.risk-copy p{font-size:15px;line-height:18.5px;margin-top:26px;width:500px}
.risk-item{left:683px;width:434px;height:68px;background:var(--panel);border-left:4px solid var(--green);border-radius:3px;color:#fff;padding:11px 24px}
.risk-item h3{font-size:17px;font-weight:600}
.risk-item p{font-size:15px;margin-top:5px}

.invest{left:0;top:1723px;width:1200px;height:450px;background:var(--light)}
.step{width:275px;height:153px;background:#fff;border-top:3px solid var(--green);padding:27px 22px 0 28px}
.step .hd{display:flex;align-items:center;gap:16px;font-size:17px;font-weight:600}
.step .n{width:34px;height:34px;border-radius:50%;background:var(--dark);color:#fff;font-size:14px;display:flex;align-items:center;justify-content:center}
.step p{font-size:15px;line-height:18.5px;color:var(--muted);margin-top:22px}

.about{left:0;top:2173px;width:1200px;height:492px}
.about-copy{left:62px;top:72px;width:530px}
.about-copy h2{font-size:28px;line-height:37px;font-weight:700;margin-top:23px}
.about-copy p{font-size:15px;line-height:18.5px;color:var(--muted);margin-top:42px;width:520px}
.focus{left:62px;top:358px;width:451px;height:80px;border:1px solid var(--line);border-radius:4px;padding:14px 0 0 23px}
.focus h3{font-size:17px;font-weight:600;color:var(--blue)}
.focus p{font-size:14.6px;color:var(--muted);margin-top:10px;white-space:nowrap}
.about-photo{left:623px;top:0;width:577px;height:492px;background:linear-gradient(135deg,#5e6b70 0%,#8d9aa0 40%,#6c8fb0 75%,#9fc1de 100%)}

.cta{left:0;top:2665px;width:1200px;height:176px;background:var(--dark-2);overflow:hidden}
.cta h2{left:67px;top:91px;color:#fff;font-size:27px;font-weight:600}
.cta .eyebrow{left:67px;top:54px}
.cta .btn{left:939px;top:65px;width:191px;height:45px}

.contact-copy{left:62px;top:2895px;width:530px}
.contact-copy h2{font-size:28px;font-weight:700;margin-top:30px}
.contact-copy p{font-size:15px;line-height:18.5px;color:var(--muted);margin-top:30px}
.contact-copy p+p{margin-top:20px}
.contact-copy address{font-style:normal;font-size:15px;line-height:18.5px;font-weight:600;color:var(--muted);margin-top:44px}
.form{left:696px;top:2892px;width:441px;height:502px;border:1px solid var(--line);border-radius:5px;padding:26px 24px}
.form label{display:block;font-size:12px;font-weight:600;color:var(--muted);margin-bottom:11px}
.row{display:flex;gap:24px;margin-bottom:15px}
.row>div{flex:1}
.form .field{height:42px}
.form .sel{color:var(--text);font-weight:600}
.form .msg{height:65px}
.form .btn{width:292px;height:45px;margin-top:25px}

.footer{left:0;top:3458px;width:1200px;height:81px;background:var(--dark);color:#fff;font-size:15px}
.footer .l{left:47px;top:30px}
.footer .r{right:45px;top:30px;display:flex;gap:25px}
</style>
</head>
<body>

<section class="hero abs">
  <div class="hero-photo abs" role="img" aria-label="Foto eines Rechenzentrums mit Serverschränken"></div>
  <div class="hero-shade abs"></div>
  <svg class="hero-cut abs" viewBox="0 0 1200 810"><polygon points="0,806 1200,766 1200,810 0,810" fill="#fff"/></svg>

  <div class="logo abs"><b>Finoval<i></i></b><span>finanzieren · klar · direkt</span></div>
  <nav class="menu abs"><span>Baufinanzierung</span><span>Versicherungen</span><span>Kapitalanlage</span><span>Über uns</span></nav>
  <div class="nav-cta btn abs">Anfrage stellen</div>

  <div class="eyebrow hero-eyebrow abs">Finanzierung für Gewerbe und Firmen</div>
  <h1 class="hero-title abs">Kapital für Rechenzentren,<br>Infrastruktur und Wachstum.</h1>
  <p class="hero-text abs">Lorem ipsum dolor sit amet, consetetur sadipscing elitr, sed diam nonumy eirmod tempor invidunt ut labore et dolore magna aliquyam erat, sed diam voluptua. At vero eos et accusam et justo duo dolores et ea rebum.</p>
  <div class="chips abs"><span class="chip">Rechenzentren</span><span class="chip">Gewerbeimmobilien</span><span class="chip">Equipment</span></div>
  <div class="hero-btns abs"><span class="btn btn-green" style="width:155px">Anfrage stellen</span><span class="btn btn-ghost" style="width:181px">Termin vereinbaren</span></div>

  <form class="quick abs">
    <div class="eyebrow">Schnellanfrage</div>
    <h2>Finanzierungsbedarf<br>prüfen lassen</h2>
    <div class="field">Name...</div>
    <div class="field">E-Mail...</div>
    <div class="field">Finanzierungsvolumen... <svg width="14" height="8" viewBox="0 0 14 8"><path d="M1 1l6 6 6-6" stroke="#444" stroke-width="1.6" fill="none"/></svg></div>
    <div class="btn btn-green">Absenden</div>
    <div class="note">Antwort in der Regel innerhalb eines Werktags.</div>
  </form>

  <div class="features abs">
    <div class="feature"><span class="ic"><svg width="22" height="22" viewBox="0 0 22 22" fill="none" stroke="#7bc143" stroke-width="1.6"><path d="M3 10l8-6 8 6v9H3z"/><path d="M8 19v-6h6v6"/></svg></span><div><h3>Gewerbe</h3><p>Finanzierungen für<br>Firmenkunden</p></div></div>
    <div class="feature"><span class="ic"><svg width="22" height="22" viewBox="0 0 22 22" fill="none" stroke="#7bc143" stroke-width="1.6"><rect x="5" y="3" width="12" height="16" rx="1"/><path d="M8 7h1M8 11h1M8 15h1M11 7h3M11 11h3M11 15h3"/></svg></span><div><h3>Rechenzentren</h3><p>Fokus auf Bau, Einrichtung<br>und Betrieb</p></div></div>
    <div class="feature"><span class="ic"><svg width="22" height="22" viewBox="0 0 22 22" fill="none" stroke="#7bc143" stroke-width="1.6"><path d="M3 3v16h16"/><path d="M6 15l4-5 3 3 5-6"/></svg></span><div><h3>Equipment</h3><p>Server, Kühlung, Energie und<br>Ausstattung finanzieren</p></div></div>
  </div>
</section>

<div class="center abs eyebrow" style="top:884px">Baufinanzierung</div>
<h2 class="center abs sec-title" style="top:922px">Strukturierte Finanzierung für gewerbliche Projekte.</h2>
<p class="center abs sec-sub" style="top:975px">Von der ersten Einordnung bis zur vermittelbaren Anfrage.</p>

<div class="card abs" style="left:62px;top:1055px;width:333px;height:207px"><div class="ico"><svg width="22" height="22" viewBox="0 0 22 22" fill="none" stroke="#fff" stroke-width="1.4"><path d="M11 4v14M6 18h10M4 7h14M6 7l-3 6h6zM16 7l-3 6h6z"/></svg></div><h3>Projektprüfung</h3><p>Analyse von Vorhaben, Kapitalbedarf,Sicherheiten und Zeithorizont.</p></div>
<div class="card abs" style="left:433px;top:1055px;width:333px;height:207px"><div class="ico"><svg width="22" height="22" viewBox="0 0 22 22" fill="none" stroke="#fff" stroke-width="1.4"><rect x="5" y="5" width="12" height="12" rx="1"/><path d="M8 9h6M8 12h6"/></svg></div><h3>Partnerzugang</h3><p>Aufbereitung für Banken, Leasingpartner und Spezialanbieter.</p></div>
<div class="card abs" style="left:803px;top:1055px;width:334px;height:207px"><div class="ico"><svg width="22" height="22" viewBox="0 0 22 22" fill="none" stroke="#fff" stroke-width="1.4"><path d="M5 6h8M5 10h5M9 15l3 3 6-8"/></svg></div><h3>Abschlussfokus</h3><p>Klare Schritte, Kommunikation und weniger Reibung.</p></div>

<section class="risk abs">
  <div class="risk-copy abs">
    <div class="eyebrow">Versicherungen</div>
    <h2>Risiken verstehen, Projekte absichern.</h2>
    <p>Lorem ipsum dolor sit amet, consetetur sadipscing elitr, sed diam nonumy eirmod tempor invidunt ut labore et dolore magna aliquyam erat, sed diam voluptua. At vero eos et accusam et justo duo dolores et ea rebum. Stet clita kasd gubergren, no sea takimata sanctus est Lorem ipsum dolor sit amet.</p>
  </div>
  <div class="risk-item abs" style="top:58px"><h3>Objekt und Betrieb</h3><p>Schutz für Gebäude, Technik und laufende Prozesse.</p></div>
  <div class="risk-item abs" style="top:145px"><h3>Verantwortung</h3><p>Prüfung relevanter Gewerbe- und Haftpflichtthemen.</p></div>
  <div class="risk-item abs" style="top:233px"><h3>Finanzierung</h3><p>Abstimmung mit Kapitalbedarf und Projektphasen.</p></div>
</section>

<section class="invest abs">
  <div class="center abs eyebrow" style="top:60px">Kapitalanlage</div>
  <h2 class="center abs sec-title" style="top:97px">Kapital strategisch einsetzen.</h2>
  <p class="center abs sec-sub" style="top:152px">Für Unternehmen, die Finanzierung, Liquidität und Anlage gemeinsam betrachten wollen.</p>
  <div class="step abs" style="left:140px;top:224px"><div class="hd"><span class="n">1</span>Zielbild</div><p>Rendite, Risiko, Laufzeit und Liquidität sauber einordnen.</p></div>
  <div class="step abs" style="left:462px;top:224px"><div class="hd"><span class="n">2</span>Optionen</div><p>Geeignete Bausteine vergleichen und verständlich erklären.</p></div>
  <div class="step abs" style="left:784px;top:224px"><div class="hd"><span class="n">3</span>Entscheidung</div><p>Nächste Schritte mit dokumentierter Grundlage vorbereiten.</p></div>
</section>

<section class="about abs">
  <div class="about-copy abs">
    <div class="eyebrow">Über Finoval</div>
    <h2>Finanzierung soll einfach zugänglich<br>und schnell entscheidbar werden.</h2>
    <p>Lorem ipsum dolor sit amet, consetetur sadipscing elitr, sed diam nonumy eirmod tempor invidunt ut labore et dolore magna aliquyam erat, sed diam voluptua. At vero eos et accusam et justo duo dolores et ea rebum. Stet clita kasd gubergren, no sea takimata sanctus est Lorem ipsum dolor sit amet.</p>
  </div>
  <div class="focus abs"><h3>Schwerpunkt Rechenzentren</h3><p>Finanzierung von Infrastruktur, Einrichtung und Wachstum.</p></div>
  <div class="about-photo abs" role="img" aria-label="Foto: zwei Geschäftsleute im Büro beim Händedruck"></div>
</section>

<section class="cta abs">
  <div class="eyebrow abs">Terminbuchung</div>
  <h2 class="abs">Bereit für ein kurzes Erstgespräch?</h2>
  <span class="btn btn-green abs">Termin vereinbaren</span>
</section>

<div class="contact-copy abs">
  <div class="eyebrow">Kontakt</div>
  <h2>Finanzierungsanfrage</h2>
  <p>Lorem ipsum dolor sit amet, consetetur sadipscing elitr, sed diam nonumy eirmod tempor invidunt ut labore et dolore magna aliquyam erat, sed diam voluptua. At vero eos et accusam et justo duo dolores et ea rebum. Stet clita kasd gubergren, no sea takimata sanctus est Lorem ipsum dolor sit amet.</p>
  <p>Lorem ipsum dolor sit amet, consetetur sadipscing elitr, sed diam nonumy eirmod tempor invidunt ut labore et dolore magna aliquyam erat, sed diam voluptua. At vero eos et accusam et justo duo dolores et ea rebum. Stet clita kasd gubergren, no sea takimata sanctus est Lorem ipsum dolor sit amet.</p>
  <address>Finoval GmbH<br>Lindenhofweg 8<br>20095 Musterstadt<br>kontakt@finoval.de</address>
</div>

<form class="form abs">
  <div class="row"><div><label>Vor- und Nachname</label><div class="field"></div></div><div><label>Firma</label><div class="field"></div></div></div>
  <div class="row"><div><label>E-Mail</label><div class="field"></div></div><div><label>Telefon</label><div class="field"></div></div></div>
  <label>Thema</label>
  <div class="field sel">Rechenzentrum finanzieren <svg width="14" height="8" viewBox="0 0 14 8"><path d="M1 1l6 6 6-6" stroke="#444" stroke-width="1.6" fill="none"/></svg></div>
  <label style="margin-top:15px">Nachricht</label>
  <div class="field msg"></div>
  <div class="btn btn-green">Absenden</div>
  <div class="note">Antwort in der Regel innerhalb eines Werktags.</div>
</form>

<footer class="footer abs">
  <div class="l abs"><b>Finoval GmbH</b>&nbsp;&nbsp; finanzieren - klar - direkt</div>
  <div class="r abs"><span>Kontakt</span><span>Impressum</span><span>Datenschutz</span></div>
</footer>

</body>
</html>
```